App UI Design: Shopping/E-commerce App

Project :
Develop an UI design & App icon for an E-commerce/Shopping App

About the App/ Target Audience:
This grocery & food shopping app will be used by independent pub, café, restaurant owners to place & manage their purchases of foods and groceries for their catering businesses.

They will use the app to access product catalogues & special promotions, search & buy large quantities of groceries or catering supplies, and the ability to manage and track status of their order.

The HTML5 App’s has been built with a very basic structure. It now needs the visual layer of the UI designed

Note:
The app is tailored for business & catering orders, not retail/supermarket buyers, so the visual needs to look smart & not too casual.
Updates

Reason: Current submissions have not met out expectations. Please use the similar app examples in the PDF as a strong point of reference for the look & feel. Feedback will be given as submissions come in, please feel free to submit initial concepts of 1 or 2 of the pages & we'll provide feedback on whether it is on the right track or not before you do more work. Current submission will also receive feedback in the next few days. We look forward to new submissions!

Target Market(s)

Male & Female. Independent pub, café, restaurant owners buying for their catering businesses. Chefs etc.

Industry/Entity Type

Restaurant

Requirements
Must have
• An overview of elements/pages of the app that needs to be designed are:
(DOWNLOAD a more detailed diagram PDF explanation)

1. Welcome- Log-in Page
2. Homepage – index that links to different function of the app

Products:
3. Promotions page – for products on special for a limited time
4. Catalogue page – access to a range of catalogue

Ways to buy:
5. Basket (Shopping Cart) - tracking items they are buying from the catalogues
6. Templates (Pre-set Shopping list)- Set shopping list that has been preloaded for certain menu
7. Open Order page

My Account:
8. My Account/profile page – Users can check the status of their order, look at past orders, look at their account number & details etc

_______________________________________________________

Icon set- Icons to represent each pages that act as visual cues for easier browsing.

2 Main features that need to be accessible & consistent throughout all pages are:
a) The Navigation Bar –
so the user can quickly find their way back & access to the main functions
b) The Search bar –
whether it drops down when needed, or is featured as a header/footer.
c) Log out button
Nice to have

Things to keep in mind:

The UI design essentially needs to be a customizable template that can easily adapt to any brand/logo with a slight change of the color scheme. As we will later implement our brand & logo onto it.

We’re looking for a clean & clear design that allows for a straight forward easy user experience.

You are free to develop different layout & UI pattern that you feel is the most efficient way the user can walk through the App & make their purchase in no more than 2 or 3 clicks
________________________________________________

Screenshot of Similar Apps for reference are also in the PDF

```html
<!DOCTYPE html>
<html lang="en">
<head>
<meta charset="utf-8">
<title>Promotions – Product Detail</title>
<link rel="stylesheet" href="https://fonts.googleapis.com/css2?family=Arimo:wght@400;700&display=swap">
<style>
  :root {
    --status-bg: #000000;
    --status-text: #ffffff;
    --header-top: #c9d1d6;
    --header-bottom: #8f9ba3;
    --header-icon: #4f5a61;
    --page-bg: #dfe4e7;
    --hero-bg: #ffffff;
    --title-band: #d3d9dd;
    --title-text: #3f474c;
    --body-bg: #f5f6f7;
    --body-text: #3a4247;
    --panel-outer: #dde3e6;
    --panel-top: #d9e0e4;
    --panel-bottom: #7f8d96;
    --panel-border: #b4bec4;
    --panel-title: #4a545a;
    --btn-round-top: #c7cfd4;
    --btn-round-bottom: #8c98a0;
    --field-bg: #ffffff;
    --field-text: #2f363a;
    --cta-top: #cfd6da;
    --cta-bottom: #7e8b94;
    --cta-text: #ffffff;
    --tab-bg-top: #2a2a2a;
    --tab-bg-bottom: #050505;
    --tab-active: #3a3a3a;
    --tab-text: #d6d6d6;
    --tab-active-text: #ffffff;
    --tab-icon: #b5b5b5;
    --accent-blue: #2e8ee0;
  }
  * { box-sizing: border-box; margin: 0; padding: 0; }
  html, body { width: 800px; height: 1200px; overflow: hidden; background: var(--page-bg); }
  body { font-family: "Arimo", Helvetica, Arial, sans-serif; position: relative; }

  .status-bar {
    position: absolute; left: 0; top: 0; width: 800px; height: 50px;
    background: var(--status-bg); color: var(--status-text);
    font-weight: 700; font-size: 28px;
  }
  .status-bar .carrier { position: absolute; left: 10px; top: 9px; display: flex; align-items: center; gap: 8px; }
  .status-bar .time { position: absolute; left: 0; right: 0; top: 9px; text-align: center; }
  .status-bar .indicators { position: absolute; right: 12px; top: 10px; display: flex; gap: 18px; align-items: center; }

  .nav-header {
    position: absolute; left: 0; top: 50px; width: 800px; height: 110px;
    background: linear-gradient(var(--header-top), var(--header-bottom));
    border-bottom: 1px solid #6e7a82;
  }
  .nav-header h1 {
    position: absolute; left: 0; right: 0; top: 26px; text-align: center;
    color: #fff; font-size: 46px; font-weight: 700;
    text-shadow: 0 -1px 1px rgba(0,0,0,0.25);
  }
  .nav-header .back { position: absolute; left: 14px; top: 32px; }
  .nav-header .home { position: absolute; right: 14px; top: 32px; }

  .product-hero {
    position: absolute; left: 0; top: 160px; width: 800px; height: 318px;
    background: var(--hero-bg);
  }
  .product-hero .photo {
    position: absolute; left: 150px; top: 25px; width: 510px; height: 285px;
    background: radial-gradient(ellipse at 50% 50%, #c79a6a 0%, #c0463c 40%, #7f9a73 70%, #ffffff 100%);
    border-radius: 40px;
  }
  .product-hero .arrow { position: absolute; top: 148px; }
  .product-hero .arrow.prev { left: 26px; }
  .product-hero .arrow.next { right: 26px; }

  .product-title-bar {
    position: absolute; left: 0; top: 478px; width: 800px; height: 82px;
    background: var(--title-band); color: var(--title-text);
    border-top: 1px solid #c3cacf; border-bottom: 1px solid #c3cacf;
  }
  .product-title-bar .name { position: absolute; left: 28px; top: 26px; font-size: 31px; font-weight: 700; }
  .product-title-bar .price { position: absolute; right: 26px; top: 28px; font-size: 26px; font-weight: 700; }

  .product-description {
    position: absolute; left: 0; top: 560px; width: 800px; height: 171px;
    background: var(--body-bg); color: var(--body-text);
    padding: 16px 26px 0 26px; font-size: 25.5px; font-weight: 700; line-height: 35px;
  }

  .order-panel {
    position: absolute; left: 0; top: 731px; width: 800px; height: 347px;
    background: var(--panel-outer);
  }
  .order-box {
    position: absolute; left: 22px; top: 19px; width: 756px; height: 328px;
    background: linear-gradient(var(--panel-top), var(--panel-bottom));
    border: 2px solid var(--panel-border); border-bottom: none;
  }
  .order-box .heading {
    height: 72px; border-bottom: 2px solid #eef1f3; text-align: center;
    font-size: 36px; font-weight: 700; color: var(--panel-title); padding-top: 16px;
    background: linear-gradient(#dfe5e8, #c9d1d6);
  }
  .stepper-btn {
    position: absolute; top: 101px; width: 64px; height: 64px; border-radius: 50%;
    background: linear-gradient(var(--btn-round-top), var(--btn-round-bottom));
    border: 2px solid #e8ecee; display: flex; align-items: center; justify-content: center;
  }
  .stepper-btn.minus { left: 205px; }
  .stepper-btn.plus { left: 488px; }
  .quantity-field {
    position: absolute; left: 287px; top: 96px; width: 185px; height: 74px;
    background: var(--field-bg); border: 2px solid #9ea9b0; border-radius: 6px;
    text-align: right; padding: 14px 16px 0 0;
    font-size: 40px; font-weight: 700; color: var(--field-text);
  }
  .add-to-basket {
    position: absolute; left: 38px; top: 194px; width: 680px; height: 102px;
    background: linear-gradient(var(--cta-top), var(--cta-bottom));
    border: 2px solid #9aa6ad; border-radius: 10px;
    text-align: center; padding-top: 24px;
    font-size: 43px; font-weight: 700; color: var(--cta-text);
    text-shadow: 0 -1px 1px rgba(0,0,0,0.3);
  }

  .tab-bar {
    position: absolute; left: 0; top: 1078px; width: 800px; height: 122px;
    background: linear-gradient(var(--tab-bg-top), var(--tab-bg-bottom));
    border-top: 2px solid #555;
  }
  .tab {
    position: absolute; top: 7px; width: 188px; height: 109px; text-align: center;
    color: var(--tab-text); font-size: 24px; font-weight: 700; border-radius: 6px;
  }
  .tab svg { display: block; margin: 6px auto 4px; }
  .tab.active { background: var(--tab-active); color: var(--tab-active-text); }
  .tab.search { left: 6px; }
  .tab.promotions { left: 205px; }
  .tab.catalogue { left: 406px; }
  .tab.basket { left: 606px; }
</style>
</head>
<body>

<div class="status-bar">
  <div class="carrier">
    <svg width="38" height="22" viewBox="0 0 38 22"><g fill="#fff"><rect x="0" y="14" width="5" height="8"/><rect x="8" y="11" width="5" height="11"/><rect x="16" y="8" width="5" height="14"/><rect x="24" y="4" width="5" height="18"/><rect x="32" y="0" width="5" height="22"/></g></svg>
    <span>Carrier</span>
  </div>
  <div class="time">10:20 PM</div>
  <div class="indicators">
    <svg width="26" height="26" viewBox="0 0 26 26"><circle cx="13" cy="13" r="12" fill="#fff"/><path d="M13 6v7h5" stroke="#000" stroke-width="2.5" fill="none"/></svg>
    <svg width="56" height="28" viewBox="0 0 56 28"><rect x="1.5" y="1.5" width="48" height="25" rx="3" fill="none" stroke="#fff" stroke-width="3"/><rect x="6" y="6" width="39" height="16" fill="#fff"/><rect x="51" y="9" width="4" height="10" fill="#fff"/></svg>
  </div>
</div>

<header class="nav-header">
  <svg class="back" width="36" height="52" viewBox="0 0 36 52"><path d="M30 4 L8 26 L30 48" stroke="var(--header-icon)" stroke-width="9" fill="none"/></svg>
  <h1>Promotions</h1>
  <svg class="home" width="58" height="50" viewBox="0 0 58 50"><path d="M29 2 L56 26 H48 V48 H35 V33 H23 V48 H10 V26 H2 Z" fill="var(--header-icon)"/><rect x="40" y="4" width="7" height="14" fill="var(--header-icon)"/></svg>
</header>

<section class="product-hero">
  <svg class="arrow prev" width="20" height="34" viewBox="0 0 20 34"><path d="M17 2 L3 17 L17 32" stroke="#b9bfc3" stroke-width="4" fill="none"/></svg>
  <div class="photo" role="img" aria-label="Product photo: wrapped gift boxes with red ribbons, pine branches and Christmas baubles"></div>
  <svg class="arrow next" width="20" height="34" viewBox="0 0 20 34"><path d="M3 2 L17 17 L3 32" stroke="#b9bfc3" stroke-width="4" fill="none"/></svg>
</section>

<div class="product-title-bar">
  <span class="name">Assorted Christmas Gifts</span>
  <span class="price">$ 32.40</span>
</div>

<p class="product-description">Proin gravida nibh vel velit auctor aliquet. Aenean sol-<br>licitudin, lorem quis bibendum auctor, nisi elit conse-<br>quat ipsum, nec sagittis sem nibh vulputate cursus a<br>sit amet mauris.</p>

<section class="order-panel">
  <div class="order-box">
    <div class="heading">Order Quantity</div>
    <div class="stepper-btn minus"><svg width="34" height="8" viewBox="0 0 34 8"><rect width="34" height="8" fill="#fff"/></svg></div>
    <div class="quantity-field">01</div>
    <div class="stepper-btn plus"><svg width="34" height="34" viewBox="0 0 34 34"><rect y="13" width="34" height="8" fill="#fff"/><rect x="13" width="8" height="34" fill="#fff"/></svg></div>
    <div class="add-to-basket">Add to Basket</div>
  </div>
</section>

<nav class="tab-bar">
  <div class="tab search">
    <svg width="68" height="68" viewBox="0 0 68 68"><circle cx="26" cy="26" r="19" fill="none" stroke="var(--tab-icon)" stroke-width="7"/><path d="M40 40 L62 62" stroke="var(--tab-icon)" stroke-width="10" stroke-linecap="round"/></svg>
    Search
  </div>
  <div class="tab promotions active">
    <svg width="68" height="68" viewBox="0 0 68 68"><path d="M8 30 H20 V64 H8 Z" fill="var(--accent-blue)"/><path d="M24 30 L36 8 C40 4 46 8 44 14 L40 26 H58 C64 26 66 32 62 36 C66 40 64 46 60 47 C63 51 60 56 56 56 C58 60 55 64 50 64 H24 Z" fill="var(--accent-blue)"/></svg>
    Promotions
  </div>
  <div class="tab catalogue">
    <svg width="68" height="68" viewBox="0 0 68 68"><rect x="14" y="4" width="44" height="60" rx="3" fill="#555" stroke="var(--tab-icon)" stroke-width="3"/><g stroke="var(--tab-icon)" stroke-width="4"><path d="M8 14 H20"/><path d="M8 26 H20"/><path d="M8 38 H20"/><path d="M8 50 H20"/></g><rect x="30" y="14" width="20" height="8" fill="var(--tab-icon)"/></svg>
    Catalogue
  </div>
  <div class="tab basket">
    <svg width="68" height="68" viewBox="0 0 68 68"><path d="M2 10 H12 L20 46 H56" stroke="var(--tab-icon)" stroke-width="4" fill="none"/><path d="M14 16 H64 L58 38 H19" stroke="var(--tab-icon)" stroke-width="3" fill="none"/><path d="M16 27 H61 M30 16 V38 M44 16 V38" stroke="var(--tab-icon)" stroke-width="2"/><circle cx="24" cy="56" r="5" fill="var(--tab-icon)"/><circle cx="50" cy="56" r="5" fill="var(--tab-icon)"/></svg>
    Basket
  </div>
</nav>

</body>
</html>
```